"Copper Horizons" poster for feature film

I need a poster for my first narrative feature film. Genre: Drama/Comedy. Synopsis: After going through a break up and moving back home, Tobias struggles through a "quarter life crisis" in pursuit of his dream of making a feature film. Tobias wants to tell a compassionate story about mental illness and its effects on a family, but the lines between fiction and reality are blurred, challenging the bond between two brothers.

Target Market(s)

Film Festivals, Prospective viewers on Vidorly/Quorvia.

Industry/Entity Type

Film Production

Other font styles liked:
• Birch STD

Colors
faa54b
f78f20
85abd2
3176b5
0355a3
fac994
f9ba93
f37122
fece3e

Requirements
Must have
• Title: Copper Horizons
• Minimalist approach.
• Please look at reference posters/prototypes.
Nice to have
• -the idea of contrasting the two brothers and the struggle of living with a mental illness.
• -the setting of the film is in Arizona, desert, living back at home as an adult.
• -the struggle of a writer. A film about a film.
• 5 phases of "The Quarter Life Crisis"
• 1. You feel trapped by your life choices, like your job, relationship, or both. You’re living on “autopilot.”
• 2. You get a sense of “I’ve got to get out of this” and feel a growing sense that change is possible if you just take a leap.
• 3. You quit the job, end the relationship, or break the commitment that’s making you feel trapped. Then you detach and enter a “time out” period where try to rediscover who you are and who you want to be.
• 4. You begin rebuilding your life slowly but surely.
• 5. You develop new commitments that are more in line with your interests and aspirations.

```html
<!DOCTYPE html>
<html lang="en">
<head>
<meta charset="utf-8">
<title>Copper Horizons — Poster</title>
<link rel="stylesheet" href="https://fonts.googleapis.com/css2?family=Lato:wght@400&family=Oswald:wght@300;400;500&display=swap">
<style>
  :root {
    --sky-teal: #6f8a88;
    --sky-slate: #4f6570;
    --sky-glow: #d9d6c4;
    --sky-copper: #c98a5c;
    --ground-dark: #2a2d33;
    --credit-gold: #f6df8a;
    --name-gold: #efe1a0;
    --title-blue: #dce9f5;
    --title-blush: #f6d2c8;
  }
  html, body {
    margin: 0;
    padding: 0;
    width: 927px;
    height: 1200px;
    overflow: hidden;
    background: var(--ground-dark);
  }
  .poster {
    position: relative;
    width: 927px;
    height: 1200px;
    overflow: hidden;
  }
  .poster svg { display: block; }
  .director-credit {
    font-family: "Lato", sans-serif;
    font-weight: 400;
    font-size: 24px;
    fill: var(--name-gold);
    letter-spacing: 0.5px;
  }
  .film-title {
    font-family: "Oswald", sans-serif;
    font-weight: 300;
    font-size: 102px;
  }
  .cast-role {
    font-family: "Oswald", sans-serif;
    font-weight: 500;
    font-size: 21px;
    fill: var(--credit-gold);
  }
  .cast-name {
    font-family: "Oswald", sans-serif;
    font-weight: 500;
    font-size: 35px;
    fill: var(--credit-gold);
  }
  .billing-block {
    font-family: "Oswald", sans-serif;
    font-weight: 400;
    fill: var(--credit-gold);
  }
  .billing-small { font-size: 16px; }
  .billing-large { font-size: 23px; font-weight: 500; }
</style>
</head>
<body>
<main class="poster">
  <svg width="927" height="1200" viewBox="0 0 927 1200" xmlns="http://www.w3.org/2000/svg">
    <defs>
      <linearGradient id="skyGradient" x1="0" y1="0" x2="1" y2="0">
        <stop offset="0" stop-color="var(--sky-slate)"/>
        <stop offset="0.35" stop-color="var(--sky-teal)"/>
        <stop offset="0.6" stop-color="var(--sky-glow)"/>
        <stop offset="1" stop-color="var(--sky-copper)"/>
      </linearGradient>
      <linearGradient id="groundFade" x1="0" y1="0" x2="0" y2="1">
        <stop offset="0" stop-color="var(--ground-dark)" stop-opacity="0"/>
        <stop offset="0.55" stop-color="var(--ground-dark)" stop-opacity="0"/>
        <stop offset="0.82" stop-color="var(--ground-dark)" stop-opacity="0.85"/>
        <stop offset="1" stop-color="var(--ground-dark)" stop-opacity="1"/>
      </linearGradient>
      <linearGradient id="figureTone" x1="0" y1="0" x2="1" y2="0">
        <stop offset="0" stop-color="#5d6a72"/>
        <stop offset="0.5" stop-color="#7a5a4c"/>
        <stop offset="1" stop-color="#c08c74"/>
      </linearGradient>
      <linearGradient id="titleGradient" x1="0" y1="0" x2="1" y2="0">
        <stop offset="0" stop-color="var(--title-blue)"/>
        <stop offset="1" stop-color="var(--title-blush)"/>
      </linearGradient>
      <filter id="softEdge" x="-5%" y="-5%" width="110%" height="110%">
        <feGaussianBlur stdDeviation="5"/>
      </filter>
    </defs>

    <rect class="sky-backdrop" width="927" height="1200" fill="url(#skyGradient)"/>

    <path class="portrait-area" role="img"
          aria-label="Photograph of a young man looking down, hand at his chin, lit by a warm desert sunset"
          d="M476 76 C600 76 672 160 668 300 C665 400 640 470 598 520 L612 540 C720 590 880 640 927 720 L927 1200 L0 1200 L0 760 C40 640 200 585 330 545 C300 495 286 420 284 320 C282 170 352 76 476 76 Z"
          fill="url(#figureTone)" opacity="0.75" filter="url(#softEdge)"/>

    <rect class="ground-fade" width="927" height="1200" fill="url(#groundFade)"/>

    <text class="director-credit" x="92" y="808">MARCUS VELDT</text>
    <text class="director-credit" x="644" y="808">MARCUS VELDT</text>

    <text class="film-title" x="50" y="918" textLength="854" lengthAdjust="spacingAndGlyphs" fill="url(#titleGradient)">COPPER HORIZONS</text>

    <g class="cast-list" text-anchor="middle">
      <text class="cast-role" x="237" y="966">ACTOR</text><text class="cast-name" x="237" y="1002">NAME</text>
      <text class="cast-role" x="359" y="966">ACTOR</text><text class="cast-name" x="359" y="1002">NAME</text>
      <text class="cast-role" x="481" y="966">ACTOR</text><text class="cast-name" x="481" y="1002">NAME</text>
      <text class="cast-role" x="604" y="966">ACTOR</text><text class="cast-name" x="604" y="1002">NAME</text>
      <text class="cast-role" x="727" y="966">ACTOR</text><text class="cast-name" x="727" y="1002">NAME</text>
    </g>

    <g class="billing-block">
      <text x="62" y="1050" textLength="822" lengthAdjust="spacingAndGlyphs"><tspan class="billing-small">LOREM IPSUM DOLOR SIT AMET </tspan><tspan class="billing-large">CONSECTETUR ADIPISICING ELIT </tspan><tspan class="billing-small">SED DO EIUSMOD TEMPOR INCIDIDUNT </tspan><tspan class="billing-large">UT LABORE ET</tspan></text>
      <text x="22" y="1081" textLength="888" lengthAdjust="spacingAndGlyphs"><tspan class="billing-large">DOLORE MAGNA </tspan><tspan class="billing-small">ALIQUA UT ENIM AD MINIM VENIAM </tspan><tspan class="billing-large">QUIS NOSTRUD EXERCITATION ULLAMCO </tspan><tspan class="billing-small">LABORIS NISI UT ALIQUIP EX EA</tspan></text>
      <text x="26" y="1112" textLength="880" lengthAdjust="spacingAndGlyphs"><tspan class="billing-small">COMMODO CONSEQUAT </tspan><tspan class="billing-large">DUIS AUTE IRURE </tspan><tspan class="billing-small">DOLOR IN REPREHENDERIT IN VOLUPTATE VELIT ESSE CILLUM </tspan><tspan class="billing-large">DOLORE EU FUGIAT NULLA</tspan></text>
      <text x="54" y="1142" textLength="824" lengthAdjust="spacingAndGlyphs"><tspan class="billing-large">PARIATUR EXCEPTEUR </tspan><tspan class="billing-small">SINT OCCAECAT CUPIDATAT </tspan><tspan class="billing-large">NON PROIDENT SUNT IN CULPA QUI </tspan><tspan class="billing-small">OFFICIA DESERUNT MOLLIT</tspan></text>
    </g>
  </svg>
</main>
</body>
</html>
```